Teaser Poster for Feature Film

We are looking for a teaser poster for our upcoming feature film P.K. GUTTER.

P.K. Gutter is a Neon Horror Satire about a flamboyant masked stranger called the P.K. Gutter who hunts and abducts celebrities who have found fame through Reality TV. The Gutter uses social networking as a platform to create an audience for his timely social statement. As events unfold, the Gutter's newly found audience grows rapidly, appreciating the lessons the Gutter inflicts on a range of victims. Each victim represents an aspect of the culture that the Gutter and the public have grown to despise. Set to a pulsing electric score, the film has an identity as unique as the Gutter himself!

SYNOPSIS:
P.K. GUTTER is a satirical take on the horror genre set against the celebrity obsessed world of modern day Los Angeles. The Gutter hates what Hollywood has become, a place where fame trumps talent, and decides to take a stand. L.A. is plunged into a state of excited trepidation as the Gutter embarks on a trail of abduction and punishment, selecting each victim to support his social statement. Every step of his journey is broadcast online using the social media that created and maintains the fame of these ‘stars’ against them. Instead of being outraged, the public supports the Gutter, empathizing with his cause. Audiences find themselves on the same journey as the flamboyant Gutter as he guides us on this humorous tale of terror.

We would like a poster that reflects the style and colors of the movie. This is not a typical horror movie, it is colourful, neon and fun. Color palette is pinks and yellows- neon.

We have included a picture of a title that we had done, which is nice, but not quite right.

We would like to have an image of Maren Tullys face, with the words....DEATH TO REALITY TV

Then below P.K. GUTTER coming soon.
It needs to be super modern and super dynamic!!!

We have included a mock up rough idea (pink background) but obviously the text P.K. GUTTER is just in a simple font on this, it needs to be something more stylized.
Feel free to stick to the outline or if you feel inspired run free!
we have also included some posters we like.

Target Market(s)

Target market is 17-30 year olds... women seem to like and get the references more, so if it was geared slightly toward women that would be helpful. Target market will have a love hate relationship with celebrity culture and reality tv. There's alot of cattiness and snark in the film.

Requirements
Must have
• The title: P.K. Gutter
• Coming Soon
• Tagline: Death to Reality TV
Nice to have
• Color palette of pinks, yellows. The opening track of the song is Quillfeather's "Kettle of Rain" -- it's got kind of an 80's glam feel to the movie. The movie has some dark elements, but it is also very funny.

```html
<!DOCTYPE html>
<html lang="en">
<head>
<meta charset="utf-8">
<title>P.K. Gutter — Teaser Poster</title>
<link rel="stylesheet" href="https://fonts.googleapis.com/css2?family=Oswald:wght@500;700&family=Teko:wght@500&display=swap">
<style>
  :root {
    --ink: #000000;
    --frame-grey: #3a3a3a;
    --muted-grey: #5c5c5c;
    --neon-pink: #e6127f;
    --neon-cyan: #14a8e0;
    --neon-yellow: #fff200;
    --neon-purple: #6d2c8c;
    --paper: #ffffff;
  }
  html, body {
    margin: 0;
    padding: 0;
    width: 840px;
    height: 1200px;
    overflow: hidden;
    background: var(--ink);
  }
  .poster {
    position: relative;
    width: 840px;
    height: 1200px;
    background: var(--ink);
    font-family: "Oswald", "Arial Narrow", sans-serif;
  }
  .frame-outer {
    position: absolute;
    inset: 24px;
    border: 3px solid var(--frame-grey);
  }
  .frame-inner {
    position: absolute;
    inset: 40px;
    border: 2px dashed var(--neon-pink);
  }
  .corner-ornament {
    position: absolute;
    width: 62px;
    height: 56px;
    background: #1c1c1c;
    border-radius: 6px;
  }
  .corner-ornament.top-left { left: 56px; top: 58px; }
  .corner-ornament.top-right { right: 56px; top: 58px; }
  .corner-ornament.bottom-left { left: 56px; bottom: 58px; }
  .corner-ornament.bottom-right { right: 56px; bottom: 58px; }

  .tagline {
    position: absolute;
    top: 86px;
    left: 0;
    right: 0;
    margin: 0;
    text-align: center;
    font-weight: 700;
    font-size: 28px;
    line-height: 40px;
    letter-spacing: 0.62em;
  }
  .tagline span { display: block; padding-left: 0.62em; }
  .tagline .word-death { color: var(--neon-pink); }
  .tagline .word-to { color: var(--neon-cyan); }
  .tagline .word-reality { color: var(--neon-yellow); }
  .tagline .word-tv { color: var(--neon-purple); }

  .portrait {
    position: absolute;
    left: 192px;
    top: 238px;
    width: 500px;
    height: 486px;
    border-radius: 46% 46% 8% 8% / 40% 40% 6% 6%;
    background:
      radial-gradient(ellipse 34% 32% at 50% 40%, var(--neon-pink) 0%, rgba(230,18,127,0.7) 55%, rgba(230,18,127,0) 100%),
      radial-gradient(ellipse 60% 55% at 50% 38%, var(--paper) 0%, var(--neon-yellow) 45%, rgba(20,168,224,0.6) 70%, rgba(0,0,0,0) 100%),
      linear-gradient(to bottom, rgba(0,0,0,0) 60%, var(--ink) 100%);
  }

  .title {
    position: absolute;
    left: 80px;
    top: 770px;
    width: 680px;
    height: 240px;
  }
  .title text {
    font-family: "Teko", "Oswald", sans-serif;
    font-weight: 500;
    font-size: 260px;
  }
  .title .title-shadow { fill: var(--neon-pink); }
  .title .title-face { fill: var(--paper); }

  .skyline {
    position: absolute;
    left: 377px;
    top: 1014px;
    width: 86px;
    height: 28px;
    background: linear-gradient(to bottom, #2e2e2e, var(--muted-grey));
    clip-path: polygon(0 100%, 0 70%, 14% 70%, 14% 45%, 24% 45%, 24% 25%, 34% 25%, 34% 55%, 44% 55%, 44% 0, 54% 0, 54% 35%, 64% 35%, 64% 15%, 74% 15%, 74% 60%, 86% 60%, 86% 75%, 100% 75%, 100% 100%);
  }
  .release-note {
    position: absolute;
    top: 1048px;
    left: 0;
    right: 0;
    margin: 0;
    text-align: center;
    color: var(--muted-grey);
    font-weight: 700;
    font-size: 17px;
    letter-spacing: 0.38em;
    padding-left: 0.38em;
  }
</style>
</head>
<body>
  <main class="poster">
    <div class="frame-outer"></div>
    <div class="frame-inner"></div>
    <div class="corner-ornament top-left" role="img" aria-label="Scrollwork corner ornament"></div>
    <div class="corner-ornament top-right" role="img" aria-label="Scrollwork corner ornament"></div>
    <div class="corner-ornament bottom-left" role="img" aria-label="Scrollwork corner ornament"></div>
    <div class="corner-ornament bottom-right" role="img" aria-label="Scrollwork corner ornament"></div>

    <h2 class="tagline">
      <span class="word-death">DEATH</span>
      <span><span class="word-to" style="display:inline;padding:0">TO&nbsp;</span><span class="word-reality" style="display:inline;padding:0">REALITY</span></span>
      <span class="word-tv">TV</span>
    </h2>

    <div class="portrait" role="img" aria-label="Neon pop-art portrait of Maren Tullys with wild platinum hair in pink, yellow and cyan"></div>

    <svg class="title" viewBox="0 0 680 240" aria-label="P.K. GUTTER">
      <text class="title-shadow" x="6" y="226" textLength="664" lengthAdjust="spacingAndGlyphs">P.K. GUTTER</text>
      <text class="title-face" x="0" y="220" textLength="664" lengthAdjust="spacingAndGlyphs">P.K. GUTTER</text>
    </svg>

    <div class="skyline" role="img" aria-label="Los Angeles skyline silhouette"></div>
    <p class="release-note">COMING SOON</p>
  </main>
</body>
</html>
```